Valdessa's New Trucking Company Website

We are wanting to create a basic website for “Valdessa Trucking” on www.ValdessaTrucking.example.

The first attachment titled “write-up” has 7 sections listed, which we would like as tabs at the top of the website, followed by the write up of that section. (The sections ‘employment’ and ‘requirements’ should be under one section).

We would like the landing page to be that of a photo of a Valdessa Truck. Please see attachment two “Valdessa_truck” as an example of what our truck looks like. We would like this to be of better quality/more pleasing to the eye. The rest of the attachments (attachment 3- attachment 7) are of possible photos/ideas.

Woould you be able to photoshop any of those trucks to look like our Valdessa Truck on to a pretty highway/background etc?

We would like this main photo be a constant background of the website, even when you click around the website and the language changes.

Target Market(s)

Northwest Based Companies seeking Transportation needs, grocery stores, Truck Drivers

Industry/Entity Type

Trucking Company

Number of Pages Required

5+ page

Font styles to use
Sans Serif

Requirements
Must have
• Must have one really good photo of our truck (or a truck that looks like ours) as the main photo on the page. This photo must stay consistent as the background when people click on the tabs/sections below.
Nice to have
• Clean/simple layout
Should not have
• Dull colors/ disorganized.

```html
<!DOCTYPE html>
<html lang="en">
<head>
<meta charset="utf-8">
<title>Valdessa Trucking</title>
<link href="https://fonts.googleapis.com/css2?family=Montserrat:wght@600;700;800&family=Open+Sans:ital,wght@0,400;0,600;0,700;1,400&family=Raleway:wght@500;600;700&display=swap" rel="stylesheet">
<style>
:root{
  --navy:#1f2a3a;
  --navy-2:#27323f;
  --footer:#262d38;
  --blue:#1565b5;
  --yellow:#f9c20a;
  --ink:#2b2b2b;
  --muted:#777;
  --light:#f7f7f7;
  --line:#e6e6e6;
}
*{margin:0;padding:0;box-sizing:border-box}
html,body{width:679px;height:1200px;overflow:hidden}
body{position:relative;background:#fff;font-family:"Open Sans",Arial,sans-serif;color:var(--ink)}
.abs{position:absolute}
.hero{left:0;top:0;width:679px;height:420px;background:var(--navy)}
.hero-photo{left:0;top:0;width:679px;height:302px;background:linear-gradient(160deg,#9a8e7a 0%,#c8b894 28%,#6d6f6c 52%,#2e3a4a 75%,#1d2735 100%)}
.hero-band{left:0;top:302px;width:679px;height:118px;background:var(--navy)}
.nav{left:138px;top:14px;width:403px;height:30px;background:#fff;box-shadow:0 1px 4px rgba(0,0,0,.2)}
.nav a{position:absolute;top:12px;font:700 4.4px Montserrat,sans-serif;color:#333;text-decoration:none;letter-spacing:.2px;white-space:nowrap}
.nav a.active{color:var(--blue)}
.nav a.active:after{content:"";position:absolute;left:-4px;right:-4px;top:-12px;height:2px;background:var(--blue)}
.search{left:380px;top:9px;width:12px;height:12px;border-radius:50%;background:var(--blue)}
.hero-bar{left:138px;top:101px;width:24px;height:2px;background:var(--yellow)}
.hero-title{left:137px;top:107px;font:800 26px/21px Montserrat,sans-serif;color:#fff;letter-spacing:.3px}
.card{width:127px;height:141px;background:#fff;top:226px}
.card-photo{left:0;top:0;width:127px;height:76px}
.readmore{right:0;top:65px;height:11px;width:58px;font:700 4.4px/11px Montserrat,sans-serif;color:#fff;padding-left:10px}
.readmore i{position:absolute;right:0;top:0;width:11px;height:11px;background:rgba(0,0,0,.25);font-style:normal;text-align:center;font-size:6px}
.card h3{position:absolute;left:10px;top:92px;font:700 6.4px Montserrat,sans-serif;color:#222}
.card h3:before{content:"";position:absolute;left:0;top:-5px;width:10px;height:1.5px;background:var(--yellow)}
.card p{position:absolute;left:10px;top:103px;width:108px;font:400 4.3px/7px "Open Sans",sans-serif;color:#666}
.btn{left:302px;top:385px;width:76px;height:16px;border-radius:8px;background:var(--yellow);font:700 4.4px/16px Montserrat,sans-serif;color:#fff;text-align:center}
.offer-title{left:0;width:679px;top:441px;text-align:center;font:600 11px Raleway,sans-serif;color:#222}
.offer-sub{left:0;width:679px;top:457px;text-align:center;font:400 4px "Open Sans",sans-serif;color:#888;letter-spacing:.3px}
.offer{width:196px;height:63px;background:var(--light)}
.offer svg{position:absolute;left:18px;top:18px}
.offer h4{position:absolute;left:58px;top:11px;font:600 6.3px Raleway,sans-serif;color:#222}
.offer p{position:absolute;left:58px;top:24px;width:128px;font:400 4.2px/7px "Open Sans",sans-serif;color:#777}
.sectors{left:0;top:645px;width:339px;height:193px;background:var(--navy-2)}
.sectors-photo{left:339px;top:645px;width:340px;height:193px;background:linear-gradient(180deg,#7fa4c9 0%,#b9cde0 45%,#a49a86 62%,#6e6a62 100%)}
.sec-bar{left:138px;top:670px;width:10px;height:1.5px;background:var(--yellow)}
.sec-title{left:138px;top:673px;font:700 7.4px Montserrat,sans-serif;color:#fff}
.sec-text{left:138px;top:689px;width:190px;font:400 4.3px/7px "Open Sans",sans-serif;color:#c7ccd3}
.sec-item{left:140px;font:400 6px "Open Sans",sans-serif;color:#fff;display:flex;align-items:center;gap:9px}
.sec-item svg{flex:none}
.col-title{top:866px;font:700 7.6px Montserrat,sans-serif;color:#222}
.news-thumb{width:35px;height:34px}
.news-date{font:400 3.8px "Open Sans",sans-serif;color:#999}
.news-head{font:400 6.4px/8.6px "Open Sans",sans-serif;color:#222;white-space:nowrap}
.more{font:700 4.2px Montserrat,sans-serif;color:var(--blue)}
.quote{left:276px;top:885px;width:127px;height:95px;background:var(--light)}
.quote p{position:absolute;left:14px;top:15px;width:100px;text-align:center;font:italic 400 4.2px/7.8px "Open Sans",sans-serif;color:#777}
.quote .qbar{position:absolute;left:55px;top:52px;width:18px;height:1.5px;background:var(--yellow)}
.quote .who{position:absolute;left:0;top:62px;width:127px;text-align:center;font:700 4.2px/7.6px Montserrat,sans-serif;color:#333}
.qnav{top:925px;width:13px;height:13px;font:700 7px/13px Montserrat,sans-serif;color:#fff;text-align:center}
.map{left:437px;top:885px;width:83px;height:52px;background:linear-gradient(135deg,#5fb3cf,#d7e4ea)}
.loc-text{left:414px;top:938px;width:127px;font:400 4.3px/7px "Open Sans",sans-serif;color:#666}
.partners{left:0;top:1002px;width:679px;height:55px;background:var(--light)}
.partner{top:1024px;font:600 6.6px "Open Sans",sans-serif;color:#8a8a8a;display:flex;align-items:center;gap:4px}
.partner b{width:8px;height:8px;background:#9a9a9a;display:block}
.footer{left:0;top:1057px;width:679px;height:143px;background:var(--footer)}
.f-title{top:1079px;font:700 5.2px Montserrat,sans-serif;color:#fff}
.f-text{font:400 4.3px/7px "Open Sans",sans-serif;color:#c5cad1}
.f-list{list-style:none;font:400 4.3px/8.6px "Open Sans",sans-serif;color:#c5cad1}
.f-list li:before{content:"› ";color:#fff}
.email{left:138px;top:1129px;width:80px;height:14px;background:#3a4350;font:italic 400 4.2px/14px "Open Sans",sans-serif;color:#aab;padding-left:6px}
.email-btn{left:218px;top:1129px;width:13px;height:14px;background:var(--blue)}
.social{top:1142px;width:10px;height:10px;border:1px solid #6c7480}
.f-rule{left:138px;top:1178px;width:403px;height:1px;background:#3a4350}
.copy{left:138px;top:1186px;font:400 3.8px "Open Sans",sans-serif;color:#aab}
</style>
</head>
<body>

<section class="abs hero">
  <div class="abs hero-photo" role="img" aria-label="Photo of a long-haul truck speeding along a highway at sunset"></div>
  <div class="abs hero-band"></div>
</section>

<nav class="abs nav">
  <a class="active" style="left:167px">HOME</a>
  <a style="left:197px">ABOUT US</a>
  <a style="left:236px">SERVICES</a>
  <a style="left:275px">NEWS</a>
  <a style="left:305px">LOCATIONS</a>
  <a style="left:347px">CONTACT</a>
  <div class="abs search"><svg width="12" height="12" viewBox="0 0 12 12"><circle cx="5.5" cy="5.5" r="2.2" fill="none" stroke="#fff" stroke-width="1"/><line x1="7.1" y1="7.1" x2="8.5" y2="8.5" stroke="#fff" stroke-width="1"/></svg></div>
</nav>

<div class="abs hero-bar"></div>
<h1 class="abs hero-title">STRONGEST<br>DISTRIBUTION<br>NETWORK</h1>

<article class="abs card" style="left:138px">
  <div class="abs card-photo" role="img" aria-label="Photo of a white truck on a motorway" style="background:linear-gradient(160deg,#9fb6cc,#dfe6ec 50%,#7c8793)"></div>
  <div class="abs readmore" style="background:var(--blue)">READ MORE<i>›</i></div>
  <h3>OVERLAND NETWORK</h3>
  <p>We have a wide experience in overland industry specific logistic solutions like farmaceutical logistics, retail and automotive logistics by train or road.</p>
</article>
<article class="abs card" style="left:275px">
  <div class="abs card-photo" role="img" aria-label="Photo of a cargo ship at sea under an evening sky" style="background:linear-gradient(180deg,#c98a5c,#e9c9a0 35%,#5b6f80 60%,#34485a)"></div>
  <div class="abs readmore" style="background:rgba(20,30,40,.55)">READ MORE<i>›</i></div>
  <h3>OCEAN FREIGHT</h3>
  <p>We bring your goods safely to worldwide destinations with our great sea fright services. We offer LLC and FLC shipments that are fast and effective with no delays.</p>
</article>
<article class="abs card" style="left:414px">
  <div class="abs card-photo" role="img" aria-label="Photo of a jet airliner flying above a city" style="background:linear-gradient(180deg,#3f7fc4,#8fbbe4 55%,#b5a78f)"></div>
  <div class="abs readmore" style="background:rgba(20,30,40,.55)">READ MORE<i>›</i></div>
  <h3>AIR FREIGHT</h3>
  <p>We provide full supply chain management package including cost effective and fast sea freight. You can also combine this package with other means of transportation.</p>
</article>

<div class="abs btn">VIEW DETAILS</div>

<h2 class="abs offer-title">What we Offer</h2>
<div class="abs offer-sub">TAILORED LOGISTIC SERVICES</div>

<div class="abs offer" style="left:138px;top:482px">
  <svg width="26" height="26" viewBox="0 0 26 26"><rect x="4" y="3" width="15" height="20" fill="none" stroke="#444" stroke-width="2"/><rect x="8" y="1" width="7" height="4" fill="#444"/><line x1="7" y1="10" x2="16" y2="10" stroke="#444" stroke-width="1.5"/><line x1="7" y1="14" x2="14" y2="14" stroke="#444" stroke-width="1.5"/><circle cx="19" cy="19" r="5" fill="var(--yellow)"/><path d="M16.5 19l2 2 3-3.5" fill="none" stroke="#fff" stroke-width="1.3"/></svg>
  <h4>Contract logistics</h4>
  <p>Cozy sphinx waves quart jug of bad milk. A very bad quack might jinx zippy fowls. Few quips galvanized the mock jury box. Quick brown dogs jump over the lazy fox. The jay, pig, fox, zebra, and my wolves quack!</p>
</div>
<div class="abs offer" style="left:345px;top:482px">
  <svg width="30" height="26" viewBox="0 0 30 26"><circle cx="10" cy="13" r="8" fill="none" stroke="#444" stroke-width="2"/><line x1="2" y1="13" x2="18" y2="13" stroke="#444" stroke-width="1.5"/><ellipse cx="10" cy="13" rx="3.5" ry="8" fill="none" stroke="#444" stroke-width="1.5"/><path d="M14 12l15-2-1 3-6 1-3 6h-2l1-5-4 1z" fill="var(--yellow)"/></svg>
  <h4>Overland, Ocean and Air Freight</h4>
  <p>To an English person, it will seem like simplified English, as a skeptical Cambridge friend of mine told me what Occidental is. The European languages are members of the same family.</p>
</div>
<div class="abs offer" style="left:138px;top:557px">
  <svg width="30" height="26" viewBox="0 0 30 26"><rect x="2" y="10" width="14" height="10" fill="var(--yellow)"/><rect x="4" y="4" width="8" height="7" fill="none" stroke="#444" stroke-width="1.5"/><line x1="19" y1="2" x2="19" y2="22" stroke="#444" stroke-width="2"/><line x1="19" y1="20" x2="28" y2="20" stroke="#444" stroke-width="2"/><circle cx="5" cy="22" r="2.5" fill="#444"/><circle cx="14" cy="22" r="2.5" fill="#444"/></svg>
  <h4>Warehousing and Storage</h4>
  <p>The jay, pig, fox, zebra, and my wolves quack! Blowzy red vixens fight for a quick jump. Five boxing wizards jump quickly in the fog. A wizard's job is to vex chumps quickly. Pack my box with five dozen liquor jugs.</p>
</div>
<div class="abs offer" style="left:345px;top:557px">
  <svg width="28" height="26" viewBox="0 0 28 26"><rect x="2" y="3" width="20" height="14" rx="1" fill="none" stroke="#444" stroke-width="2"/><line x1="12" y1="17" x2="12" y2="22" stroke="#444" stroke-width="2"/><line x1="7" y1="22" x2="17" y2="22" stroke="#444" stroke-width="2"/><path d="M17 12v-4a1.5 1.5 0 0 1 3 0v5h3a2 2 0 0 1 2 2v5a4 4 0 0 1-4 4h-3l-4-5z" fill="var(--yellow)"/></svg>
  <h4>Consulting Services</h4>
  <p>The Big Oxmox advised her not to do so, because there were thousands of bad Commas, wild Question Marks and devious Semikoli, but the Little Blind Text didn't listen. She packed her seven versalia.</p>
</div>

<section class="abs sectors"></section>
<div class="abs sectors-photo" role="img" aria-label="Photo of a white semi truck with flatbed trailer on a desert highway"></div>
<div class="abs sec-bar"></div>
<h2 class="abs sec-title">INDUSTRY SECTORS COVERAGE</h2>
<p class="abs sec-text">We cover different industry sectors, from food and beverage, chemical, retail, durable goods and more. Check the full list.</p>
<div class="abs sec-item" style="top:713px"><svg width="12" height="14" viewBox="0 0 12 14"><rect x="2" y="5" width="8" height="8" fill="#fff"/><rect x="3" y="1" width="6" height="4" fill="var(--yellow)"/></svg>Consumer Packaged Goods</div>
<div class="abs sec-item" style="top:734px"><svg width="12" height="14" viewBox="0 0 12 14"><rect x="1" y="2" width="10" height="11" rx="1" fill="#fff"/><circle cx="6" cy="8" r="2.5" fill="var(--yellow)"/></svg>Chemical Goods</div>
<div class="abs sec-item" style="top:755px"><svg width="14" height="14" viewBox="0 0 14 14"><rect x="1" y="4" width="4" height="9" fill="#fff"/><ellipse cx="10" cy="6" rx="3.5" ry="2" fill="var(--yellow)"/><rect x="6.5" y="6" width="7" height="7" fill="var(--yellow)"/></svg>Food and Beverage</div>
<div class="abs sec-item" style="top:776px"><svg width="14" height="14" viewBox="0 0 14 14"><path d="M2 4h10l-1 9H3z" fill="#fff"/><path d="M4.5 4a2.5 2.5 0 0 1 5 0" fill="none" stroke="var(--yellow)" stroke-width="1.5"/></svg>Retail Goods</div>
<div class="abs sec-item" style="top:798px"><svg width="22" height="14" viewBox="0 0 22 14"><rect x="1" y="3" width="8" height="7" fill="#fff"/><ellipse cx="15" cy="6" rx="6" ry="4" fill="var(--yellow)"/><circle cx="4" cy="12" r="1.8" fill="#fff"/><circle cx="16" cy="12" r="1.8" fill="#fff"/></svg>Energy, Oil and Gas</div>

<h2 class="abs col-title" style="left:138px">COMPANY NEWS</h2>
<h2 class="abs col-title" style="left:276px">WHAT CLIENTS SAY</h2>
<h2 class="abs col-title" style="left:414px">OUR LOCATIONS</h2>

<div class="abs news-thumb" style="left:138px;top:884px;background:linear-gradient(160deg,#b88a5a,#3a3f48)" role="img" aria-label="Photo of a truck at dusk"></div>
<div class="abs news-date" style="left:180px;top:885px"><span style="color:var(--yellow)">▪</span> APRIL 22, 2015</div>
<div class="abs news-head" style="left:180px;top:892px">New service available:<br>end-to-end logistics</div>
<div class="abs more" style="left:234px;top:914px">READ MORE ›</div>
<div class="abs news-thumb" style="left:138px;top:926px;background:linear-gradient(160deg,#e8ecef,#a9b7c2)" role="img" aria-label="Photo of financial charts on paper"></div>
<div class="abs news-date" style="left:180px;top:927px"><span style="color:var(--yellow)">▪</span> APRIL 22, 2015</div>
<div class="abs news-head" style="left:180px;top:934px">First quartal 2015 revenue<br>report released</div>
<div class="abs more" style="left:234px;top:956px">READ MORE ›</div>
<div class="abs" style="left:238px;top:972px;font:italic 400 4.2px 'Open Sans',sans-serif;color:#999">Read all news</div>

<div class="abs quote">
  <p>Best customer support and response time I have ever seen... not to mention a kick ass service! Great feeling from this partnership. Thank you Valdessa Trucking!</p>
  <div class="qbar"></div>
  <div class="who">MARCUS HALE,<br>TIDEWELL FREIGHT &amp; LOGISTICS SOLUTIONS</div>
</div>
<div class="abs qnav" style="left:276px;background:#2b3440">‹</div>
<div class="abs qnav" style="left:390px;background:var(--yellow)">›</div>

<div class="abs map" role="img" aria-label="Illustration of a world map with location pins and a delivery truck"></div>
<p class="abs loc-text">Valdessa Trucking covers over 150 locations all over the globe plus numerous logistic partner companies from different areas of supply chain.</p>
<div class="abs more" style="left:487px;top:964px">VIEW ALL LOCATIONS <svg width="4" height="5" viewBox="0 0 4 5"><path d="M2 5L.3 2.3A1.8 1.8 0 1 1 3.7 2.3z" fill="var(--blue)"/></svg></div>

<section class="abs partners"></section>
<div class="abs partner" style="left:138px;color:#2a6f8f"><b style="background:#2aa7a0"></b>NORVALE</div>
<div class="abs partner" style="left:211px">BRICKFIELD</div>
<div class="abs partner" style="left:276px"><b></b>TIDEWELL</div>
<div class="abs partner" style="left:345px">Loopmark</div>
<div class="abs partner" style="left:414px"><b></b>CARGOLINE</div>
<div class="abs partner" style="left:484px">Greenleaf</div>

<footer class="abs footer"></footer>
<h3 class="abs f-title" style="left:138px">NEWSLETTER SUBSCRIBE</h3>
<p class="abs f-text" style="left:138px;top:1093px;width:92px">Subscribe to our newsletter and we will inform you about newset projects and promotions.</p>
<div class="abs email">Your email address</div>
<div class="abs email-btn"><svg width="13" height="14" viewBox="0 0 13 14"><rect x="3.5" y="5" width="6" height="4" fill="none" stroke="#fff" stroke-width=".8"/><path d="M3.5 5l3 2.2 3-2.2" fill="none" stroke="#fff" stroke-width=".8"/></svg></div>

<h3 class="abs f-title" style="left:241px">QUICK LINKS</h3>
<ul class="abs f-list" style="left:241px;top:1092px">
  <li>About us</li><li>Supply Chain Management</li><li>Company News</li><li>Promotions</li><li>Consulting Services</li><li>Privacy Policy</li><li>Track your Package</li>
</ul>
<h3 class="abs f-title" style="left:345px">INDUSTRY SOLUTIONS</h3>
<ul class="abs f-list" style="left:345px;top:1092px">
  <li>Automotive</li><li>Chemicals</li><li>Energy, Oil and Gas</li><li>Food and Beverages</li><li>Retail Goods</li><li>Pharmaceutical</li><li>Consumer Goods</li>
</ul>
<h3 class="abs f-title" style="left:449px">CONTACT US</h3>
<p class="abs f-text" style="left:449px;top:1094px">48 Harbor Lane,<br>Portland, Oregon</p>
<p class="abs" style="left:449px;top:1115px;font:400 6px 'Open Sans',sans-serif;color:#fff">+1 503 555 0148</p>
<p class="abs f-text" style="left:449px;top:1125px">info@valdessatrucking.example</p>
<div class="abs social" style="left:449px"></div>
<div class="abs social" style="left:462px"></div>
<div class="abs social" style="left:475px"></div>
<div class="abs f-rule"></div>
<p class="abs copy">VALDESSA TRUCKING 2015. ALL RIGHTS RESERVED</p>

</body>
</html>
```